Simple fencing and steel manufacturing website

** update 01/04/2015 ** we did not add logo design, but if your font/logo is accepted we will add $50 to make it more fair
Even if you web design is not chosen, but your logo is, we will pay you $50. If both are chosen you will get an extra $50
Open brief

Site map:
Home
About
Gallery
-photos
-testimonials
Contact

No current website:

No current logo, colors currently black and gold but we don't mind changing them - wide open brief
Happy for new font/style/logo for company name which is Paling Brightway

Customer wants clean, credible and professional look & feel
stock photos OK

Brief:

One home page - simple with 2 or 3 small areas to tease and attract the user and one template page to suit all the other pages

All competitor websites are pretty bad, the best of them is
http://www.wexmoorrailing.com.au/index.html

Target Market(s)

Government and top level builders

Industry/Entity Type

Fencing

Requirements
Must have
• 1. Display ISO and environmental awards (ISO9001 AS4801 ISO14001)
• 2. A list of about 15 products
• Can be in teaser areas of home page as suggested before or slider or really anywhere
Nice to have
• Log with name - nice but not necessary (we don't have one)

```html
<!DOCTYPE html>
<html lang="en">
<head>
<meta charset="utf-8">
<title>Paling Brightway</title>
<link rel="stylesheet" href="https://fonts.googleapis.com/css2?family=Open+Sans:wght@400;600;700&display=swap">
<style>
:root{
  --gold:#c9a53a;
  --gold-dark:#a8872a;
  --gold-soft:#e9dcae;
  --ink:#1a1a1a;
  --black:#111111;
  --text:#555555;
  --muted:#8a8a8a;
  --white:#ffffff;
  --card-bg:#f4f4f4;
}
*{box-sizing:border-box;margin:0;padding:0}
html,body{width:1200px;height:2200px;overflow:hidden}
body{font-family:"Open Sans",Arial,sans-serif;color:var(--text);background:var(--white)}

.site-header{height:160px;position:relative;background:var(--white)}
.brand{position:absolute;left:0;right:0;top:58px;display:flex;align-items:center;justify-content:center;gap:12px}
.brand-mark{width:18px;height:18px;background:var(--gold)}
.brand-name{font-weight:700;font-size:28px;letter-spacing:1px;color:var(--ink);text-transform:uppercase;line-height:1}
.header-contact{position:absolute;right:40px;top:10px;text-align:right}
.social{display:flex;gap:8px;justify-content:flex-end;margin-bottom:48px}
.social span{width:20px;height:20px;border-radius:50%;background:var(--gold)}
.phone{font-size:20px;color:var(--ink);display:flex;align-items:center;gap:10px}
.phone small{font-size:15px;color:var(--muted)}
.phone svg{width:20px;height:20px}

.main-nav{height:40px;background:var(--black);display:flex;align-items:center;padding-left:150px}
.main-nav a{color:var(--white);text-decoration:none;font-size:15px;font-weight:600;text-transform:uppercase;padding:0 28px;line-height:40px}
.main-nav a.active{background:#000}

.hero{position:relative;height:540px}
.hero-photo{position:absolute;inset:0;background:linear-gradient(180deg,#dfe6ea 0%,#c6d0c8 30%,#6f8f5a 55%,#3f6a2e 100%)}
.hero-content{position:absolute;left:0;right:0;top:150px;text-align:center;color:var(--white)}
.hero-title{font-size:80px;font-weight:600;line-height:1}
.hero-sub{font-size:60px;font-weight:400;margin-top:6px}
.hero-actions{display:flex;justify-content:center;gap:80px;margin-top:34px}
.btn{display:inline-block;width:240px;height:54px;line-height:50px;font-size:24px;color:var(--white);text-decoration:none;text-align:center;border:2px solid var(--white)}
.btn-dark{background:rgba(0,0,0,.55)}
.btn-gold{background:var(--gold);border-color:var(--gold)}

.why{padding:70px 120px 30px;text-align:center}
.why h2{color:var(--gold);font-size:30px;font-weight:400;margin-bottom:34px}
.why p{font-size:13px;line-height:1.7;margin-bottom:18px}

.features{display:flex;justify-content:center;gap:52px;padding:20px 0 40px}
.feature-card{width:296px;height:310px;background:var(--card-bg);box-shadow:0 2px 6px rgba(0,0,0,.18);position:relative;text-align:center;padding-top:14px}
.feature-card h3{color:var(--gold);font-size:20px;font-weight:600;margin-bottom:8px}
.feature-photo{display:block;width:256px;height:120px;margin:0 auto 10px}
.photo-a{background:linear-gradient(160deg,#c6d3dc,#8a7a5e)}
.photo-b{background:linear-gradient(160deg,#d7c4a0,#8d6b3c)}
.photo-c{background:linear-gradient(160deg,#c9d7e3,#b08a52)}
.feature-card p{font-size:11px;line-height:1.6;padding:0 22px}
.more{position:absolute;left:108px;bottom:-4px;width:80px;height:30px;line-height:30px;background:var(--gold);color:var(--white);font-size:12px;font-weight:700;border-radius:4px 4px 0 0}

.products{height:360px;background:linear-gradient(180deg,#f6f0dc 0%,var(--gold-soft) 55%,#d4bd72 100%);text-align:center;padding-top:26px;position:relative}
.products h2{color:var(--gold-dark);font-size:36px;font-weight:400}
.products .lead{font-size:16px;color:var(--ink);margin:10px 0 20px}
.product-row{display:flex;justify-content:center;gap:16px}
.product-photo{width:250px;height:220px}
.pp1{background:linear-gradient(170deg,#b9cbd9,#7d8a94)}
.pp2{background:linear-gradient(170deg,#a9bccf,#5a6470)}
.pp3{background:linear-gradient(170deg,#c1cdd6,#8c7a5a)}
.pp4{background:linear-gradient(170deg,#bfcfdd,#6e7880)}
.arrow{position:absolute;top:200px;width:26px;height:40px;background:var(--black);display:flex;align-items:center;justify-content:center}
.arrow.left{left:14px}.arrow.right{right:14px}
.arrow svg{width:12px;height:16px}

.gap{height:50px;background:var(--white)}

.site-footer{height:230px;background:var(--black);color:var(--white);display:flex;padding:30px 0 0 110px}
.footer-col h4{color:var(--gold);font-size:24px;font-weight:400;margin-bottom:16px}
.footer-links{width:330px}
.footer-links ul{list-style:none;display:grid;grid-template-columns:170px 130px;row-gap:6px}
.footer-links li{font-size:13px}
.footer-form{width:400px}
.form-grid{display:grid;grid-template-columns:190px 190px;gap:10px}
.field{height:24px;background:var(--white);color:var(--muted);font-size:11px;padding:4px 6px}
.field.tall{grid-row:span 2;height:58px}
.submit{grid-column:2;justify-self:end;width:90px;height:28px;line-height:28px;background:var(--gold);text-align:center;font-size:13px}
.footer-contact{width:260px;position:relative}
.footer-contact p{font-size:12px;line-height:1.6}
.footer-contact strong{font-weight:700}
.footer-brand{position:absolute;right:-20px;top:150px;display:flex;align-items:center;gap:6px;font-size:11px;font-weight:600;color:var(--gold);text-transform:uppercase}
.footer-brand i{width:10px;height:10px;background:var(--gold)}
.copyright{height:40px;background:#000;color:#bbbbbb;font-size:12px;line-height:40px;padding-left:110px}
</style>
</head>
<body>

<header class="site-header">
  <div class="brand">
    <span class="brand-mark"></span>
    <span class="brand-name">Paling Brightway</span>
  </div>
  <div class="header-contact">
    <div class="social"><span></span><span></span><span></span><span></span><span></span></div>
    <div class="phone"><small>Call us</small>
      <svg viewBox="0 0 24 24"><path fill="#1a1a1a" d="M6.6 10.8a15 15 0 0 0 6.6 6.6l2.2-2.2c.3-.3.7-.4 1-.2 1.1.4 2.3.6 3.6.6.6 0 1 .4 1 1V20c0 .6-.4 1-1 1A17 17 0 0 1 3 4c0-.6.4-1 1-1h3.5c.6 0 1 .4 1 1 0 1.3.2 2.5.6 3.6.1.3 0 .7-.2 1z"/></svg>
      719-555-0142</div>
  </div>
</header>

<nav class="main-nav">
  <a class="active" href="#">Home</a>
  <a href="#">About Us</a>
  <a href="#">Why Paling Brightway</a>
  <a href="#">Products</a>
  <a href="#">Contact</a>
</nav>

<section class="hero">
  <div class="hero-photo" role="img" aria-label="Chain-link fence along a green sports field"></div>
  <div class="hero-content">
    <div class="hero-title">The Best Performances</div>
    <div class="hero-sub">over the years</div>
    <div class="hero-actions">
      <a class="btn btn-dark" href="#">More Information</a>
      <a class="btn btn-gold" href="#">Our Products</a>
    </div>
  </div>
</section>

<section class="why">
  <h2>Why work Paling Brightway?</h2>
  <p>Working from the largest database of industry professionals across Australia, our team operates exclusively in the mining, oil and gas, construction and engineering sectors. Our clients range from engineering consultancies and major owner-operator oil companies to international contractors and the largest diversified mining companies in the world. In addition to providing health, safety, environment and quality professionals, we also deliver highly qualified and experienced risk management, emergency response and training personnel at all levels.</p>
  <p>Today's dynamic and ever-changing workplace requires recruiters to be up to the task, and that is where we come in. With offices in Perth, Brisbane and Hong Kong, we source both locally and internationally to meet the unique requirements of our clients and candidates. Our passion for the industry and commitment to ensuring a safer work environment for all is the foundation of everything we do.</p>
</section>

<section class="features">
  <article class="feature-card">
    <h3>LIPSUM IPSUM</h3>
    <div class="feature-photo photo-a" role="img" aria-label="Engineers reviewing plans on a building site"></div>
    <p>Vestibulum rutrum pharetra diam, eget dapibus leo vehicula ut. Fusce aliquam, odio eget ornare leo diam, eget dapibus leo vehicula ut.</p>
    <span class="more">MORE</span>
  </article>
  <article class="feature-card">
    <h3>LIPSUM IPSUM</h3>
    <div class="feature-photo photo-b" role="img" aria-label="Worker cutting timber with a power saw"></div>
    <p>Vestibulum rutrum pharetra diam, eget dapibus leo vehicula ut. Fusce aliquam, odio eget ornare leo diam, eget dapibus leo vehicula ut.</p>
    <span class="more">MORE</span>
  </article>
  <article class="feature-card">
    <h3>LIPSUM IPSUM</h3>
    <div class="feature-photo photo-c" role="img" aria-label="Builders installing a timber roof frame"></div>
    <p>Vestibulum rutrum pharetra diam, eget dapibus leo vehicula ut. Fusce aliquam, odio eget ornare leo diam, eget dapibus leo vehicula ut.</p>
    <span class="more">MORE</span>
  </article>
</section>

<section class="products">
  <h2>We Our Products</h2>
  <p class="lead">Since the inception of the firm in the year 1999 PBW has developed into one of the innovative</p>
  <div class="product-row">
    <div class="product-photo pp1" role="img" aria-label="Steel structure under construction"></div>
    <div class="product-photo pp2" role="img" aria-label="Construction crew on scaffolding"></div>
    <div class="product-photo pp3" role="img" aria-label="Crane lifting steel beams"></div>
    <div class="product-photo pp4" role="img" aria-label="Tower crane over a building site"></div>
  </div>
  <span class="arrow left"><svg viewBox="0 0 12 16"><path d="M10 1 3 8l7 7" fill="none" stroke="#fff" stroke-width="2.5"/></svg></span>
  <span class="arrow right"><svg viewBox="0 0 12 16"><path d="m2 1 7 7-7 7" fill="none" stroke="#fff" stroke-width="2.5"/></svg></span>
</section>

<div class="gap"></div>

<footer class="site-footer">
  <div class="footer-col footer-links">
    <h4>Navigation Links</h4>
    <ul>
      <li>Home</li><li>Products</li>
      <li>About Us</li><li>Contact Us</li>
      <li>Why Paling Brightway</li><li></li>
      <li>Services</li><li></li>
    </ul>
  </div>
  <div class="footer-col footer-form">
    <h4>Contact Form</h4>
    <div class="form-grid">
      <div class="field">Name</div>
      <div class="field tall">Comments</div>
      <div class="field">Email Address</div>
      <span class="submit">Submit</span>
    </div>
  </div>
  <div class="footer-col footer-contact">
    <h4>Contact Us</h4>
    <p><strong>12 Kestrel Lane</strong><br>Marwick NSW 2571<br>Mobile: 0400 555 218<br>Email: info@palingbrightway.example</p>
    <div class="footer-brand"><i></i>Paling Brightway</div>
  </div>
</footer>
<div class="copyright">Copyright © 2014 Paling Brightway. All right reserved.</div>

</body>
</html>
```